Business card for Property Management consultant

I need a business card for my business LX Vantage - I consult to real estate agents to improve the performance of their Property Management departments (rental houses management). The card needs to be very professional looking, incorporating our logo and my photo plus the line "Develop your Rent Roll to Perform"

Target Market(s)

Real Estate business owners

Industry/Entity Type

Business Consultant

Contact Information for Business Card

Business name - LX Vantage (logo uploaded)
My Name : Marcia Kellaway -
Title : Property Management Consultant

Develop your Rent Roll to perform

Phone : +61 438592716
email : marcia@lxvantage.com.au
website ; www.lxvantage.com.au

Requirements
Must have
• Logo
• My photo
• Very corporate / professional look

```html
<!DOCTYPE html>
<html lang="en">
<head>
<meta charset="utf-8">
<title>LX Vantage – Business Card</title>
<link rel="stylesheet" href="https://fonts.googleapis.com/css2?family=Lato:ital,wght@0,400;0,700;0,900;1,400&display=swap">
<style>
  :root {
    --backdrop: #e4e6ea;
    --card: #ffffff;
    --ink: #1c1c1c;
    --brand-blue: #2b5fb4;
    --rule-blue: #3a63b8;
    --brand-gold: #c9912c;
    --photo-warm: #8a4a32;
    --photo-skin: #e3b49f;
    --photo-blue: #2456c4;
  }
  * { box-sizing: border-box; margin: 0; padding: 0; }
  html, body {
    width: 1200px; height: 900px; overflow: hidden;
    background: var(--backdrop);
    font-family: "Lato", sans-serif;
    color: var(--ink);
  }
  .stage {
    width: 1200px; height: 900px;
    display: flex; align-items: center; justify-content: center;
  }
  .business-card {
    position: relative;
    width: 900px; height: 520px;
    background: var(--card);
    box-shadow: 0 18px 40px rgba(20, 30, 60, 0.18);
    overflow: hidden;
  }
  .portrait {
    position: absolute; left: 40px; bottom: 0;
    width: 340px; height: 440px;
    border-radius: 150px 150px 0 0;
    background: linear-gradient(180deg,
      var(--photo-warm) 0%,
      var(--photo-skin) 45%,
      var(--photo-blue) 72%,
      var(--photo-blue) 100%);
  }
  .brand {
    position: absolute; right: 60px; top: 52px;
    display: flex; align-items: center; gap: 16px;
    padding-bottom: 12px;
    border-bottom: 3px solid var(--rule-blue);
  }
  .brand-mark {
    width: 32px; height: 32px;
    background: var(--brand-gold);
  }
  .brand-name {
    font-weight: 900; font-size: 46px; letter-spacing: 0.5px;
    color: var(--ink); line-height: 1;
  }
  .details {
    position: absolute; right: 60px; top: 150px;
    width: 440px;
    text-align: right;
  }
  .tagline {
    font-size: 25px; font-weight: 400; margin-bottom: 20px;
    white-space: nowrap;
  }
  .person-name {
    font-size: 36px; font-weight: 700; color: var(--brand-blue); line-height: 1.15;
  }
  .person-title {
    font-size: 21px; font-style: italic; margin-bottom: 24px;
  }
  .contact-list { list-style: none; font-size: 22px; line-height: 1.4; }
</style>
</head>
<body>
  <main class="stage">
    <section class="business-card">
      <div class="portrait" role="img" aria-label="Portrait photo of Marcia Kellaway in a blue jacket"></div>

      <div class="brand">
        <span class="brand-mark"></span>
        <span class="brand-name">LX Vantage</span>
      </div>

      <div class="details">
        <p class="tagline">Develop Your Rent Roll To Perform</p>
        <h1 class="person-name">Marcia Kellaway</h1>
        <p class="person-title">Property Management Consultant</p>
        <ul class="contact-list">
          <li class="contact-phone">+61 43859 2716</li>
          <li class="contact-web">www.lxvantage.com.au</li>
          <li class="contact-email">marcia@lxvantage.com.au</li>
        </ul>
      </div>
    </section>
  </main>
</body>
</html>
```